CD Cover Design Project

Don't have a huge brief or visual idea of exactly what i want, but here are the details:

Band Name: The Brinewalkers
Title: Nearly Every Road Back Home
Genre: indie rock - think Painted In Tunnels, Marrow, Pemby, The Torvals, etc)

Definitely want the name and title on the cover. It could be more photography based or design based. A little more abstract. Totally open. Brinewalkers chew up everything they see... One thought was an eaten, old beat up guitar...maybe too cliche.

Album covers i love: Quietfall, Harbour Signals, Ignore All Rhubarb Prophets, Rusted Ladders, Keep Us Warm

Happy to send music or give feedback on concepts prior to working on them...not sure of the rules...whatever is within them.

```html
<!DOCTYPE html>
<html lang="en">
<head>
<meta charset="utf-8">
<title>The Brinewalkers – Nearly Every Road Back Home</title>
<link rel="stylesheet" href="https://fonts.googleapis.com/css2?family=Federant&family=Open+Sans:wght@400;600&display=swap">
<style>
  :root {
    --wood-deep: #0c0d07;
    --wood-dark: #221d0c;
    --wood-mid: #3f3714;
    --wood-olive: #5b5220;
    --wood-glow: #7f7234;
    --bar-black: #030303;
    --bar-green: #0e1712;
    --seam: #020202;
    --title-stroke: #c3c6c6;
    --title-fill: #16140c;
    --band-text: #f0f0f0;
    --plate-red: #7a2a1a;
    --plate-text: #e6cdb4;
    --ghost: rgba(205, 165, 55, 0.45);
  }
  * { margin: 0; padding: 0; box-sizing: border-box; }
  html, body { width: 1200px; height: 1200px; overflow: hidden; background: #000; }
  .cover {
    position: relative;
    width: 1200px;
    height: 1200px;
    overflow: hidden;
  }
  .door-photo {
    position: absolute;
    inset: 0;
    background:
      radial-gradient(ellipse 70% 75% at 50% 42%, transparent 40%, rgba(5,6,3,0.85) 100%),
      radial-gradient(ellipse 22% 30% at 58% 44%, rgba(150,140,80,0.55) 0%, transparent 100%),
      radial-gradient(ellipse 34% 40% at 46% 36%, var(--wood-glow) 0%, rgba(91,82,32,0.7) 45%, transparent 100%),
      linear-gradient(90deg, var(--wood-dark) 0%, var(--wood-mid) 30%, var(--wood-olive) 50%, var(--wood-mid) 72%, var(--wood-dark) 100%),
      var(--wood-deep);
  }
  .door-seam {
    position: absolute;
    left: 590px;
    top: 0;
    width: 9px;
    height: 1200px;
    background: var(--seam);
    box-shadow: 0 0 6px rgba(0,0,0,0.8);
  }
  .ghost-title {
    position: absolute;
    left: 420px;
    top: 118px;
    width: 115px;
    font-family: "Federant", serif;
    font-size: 58px;
    line-height: 1;
    text-align: left;
    color: transparent;
    -webkit-text-stroke: 1.5px var(--ghost);
    transform: scaleX(-1);
  }
  .ghost-title span { display: block; height: 200px; }
  .album-title {
    position: absolute;
    right: 62px;
    top: 52px;
    font-family: "Federant", serif;
    font-weight: 400;
    font-size: 74px;
    line-height: 108px;
    text-align: right;
    color: var(--title-fill);
    -webkit-text-stroke: 1.5px var(--title-stroke);
    text-shadow: 3px 4px 6px rgba(0,0,0,0.85);
    transform: scaleX(0.8);
    transform-origin: right top;
  }
  .album-title span { display: block; }
  .band-bar {
    position: absolute;
    left: 0;
    top: 678px;
    width: 567px;
    height: 67px;
    background: var(--bar-black);
    display: flex;
    align-items: center;
    padding-left: 42px;
  }
  .band-name {
    font-family: "Open Sans", sans-serif;
    font-weight: 400;
    font-size: 46px;
    color: var(--band-text);
    white-space: nowrap;
  }
  .handle-bar {
    position: absolute;
    left: 648px;
    top: 673px;
    width: 552px;
    height: 77px;
    background: var(--bar-green);
  }
  .pull-plate {
    position: absolute;
    left: 627px;
    top: 638px;
    width: 106px;
    height: 38px;
    background: var(--plate-red);
    border: 2px solid #4a160c;
    display: flex;
    align-items: center;
    justify-content: center;
    font-family: "Open Sans", sans-serif;
    font-weight: 600;
    font-size: 19px;
    color: var(--plate-text);
    letter-spacing: 1px;
  }
</style>
</head>
<body>
  <main class="cover">
    <div class="door-photo" role="img" aria-label="Photograph of weathered wooden double doors with peeling olive paint and dark red streaks, lit from the centre"></div>
    <div class="door-seam"></div>
    <div class="ghost-title" aria-hidden="true">
      <span>Nearly</span><span>Every</span><span>Road</span>
    </div>
    <h1 class="album-title">
      <span>Nearly</span><span>Every</span><span>Road</span><span>Back</span><span>Home</span>
    </h1>
    <div class="handle-bar"></div>
    <div class="pull-plate">PULL</div>
    <div class="band-bar"><h2 class="band-name">The Brinewalkers</h2></div>
  </main>
</body>
</html>
```